12 Week Brisk Peak Lean Form Challenge Flyer

Hi,
We are a tennis coaching business called Vantle Racquet based in Sydney Australia. We are looking to launch a new 12 week fitness program called "12 Week Brisk Peak Form Lean Challenge"
We would like the flyer to utilise the colours green and yellow reflecting the tennis theme - however we don't necessarily want it to look like a tennis flyer as tennis is only a small piece of the program via our tennis cardio workouts. We are using tennis cardio as a fitness thing.
We are based in Australia where spring is about to start and everyone is looking to get fit and beach ready for summer so we would like the flyer to communicate fitness, energy, vitality etc. = a Brisk Peak Life !
SPECIFICALLY ON THE FLYER WE WOULD LIKE THE FOLLOWING INFO:
Get a Brisk Peak Form. Live a Brisk Peak Life. In Just 12 Weeks.
Take the challenge today !
Your challenge should you choose to accept it will include:
3 weekly 1hr group training sessions using fast, high intensity & seriously fun cardio workouts. with music to pump you up.
90 Day weight management & nutrition plan using revolutionary nutritional, all natural products. (All products included)
12 Week E-Course covering the dieting dilemma, exercise, stress management and sleep.
Personalised & interactive online membership program which includes:
- Customised meal plans based on your personal nutrition parameters & food preferences
- Step by Step guide to achieving your health goals
- Interactive goal setting charts to track your progress
- Delicious recipe database & thousands of meal options
- Easy interactive nutrition and exercise journal
- Full nutrition support from our team of experts
It's time to take action & get Brisk Peak Form Lean !
Only $99 per week !!
Join TODAY
Starts September 17th.
Call 02 7381 2459 or email us at info@vantleracquet.example
Please let us know if you need any more info.
Our website is www.vantleracquet.example if you want to see more about us but again please keep in mind this is not being marketed as a tennis specific program ... more of a fitness, get ready for summer program.
Thanks
Gwendolyn
Target Market(s)
Men and women between ages of 27-45 years
Industry/Entity Type
Nutrition

```html
<!DOCTYPE html>
<html lang="en">
<head>
<meta charset="utf-8">
<title>12 Week Brisk Peak Lean Form Challenge</title>
<link rel="stylesheet" href="https://fonts.googleapis.com/css2?family=Josefin+Sans:wght@700&family=Dosis:wght@300;400;700&family=Homemade+Apple&display=swap">
<style>
  :root {
    --ink: #000000;
    --white: #ffffff;
    --green: #8cc63f;
    --gold: #f6a921;
    --grey: #8a8a8a;
    --silhouette: #4a4a4a;
    --body: #e6e6e6;
  }
  html, body { margin: 0; padding: 0; background: var(--ink); overflow: hidden; }
  .flyer {
    position: relative; width: 927px; height: 1200px; overflow: hidden;
    background: var(--ink); color: var(--white);
    font-family: "Dosis", "Arial Narrow", sans-serif;
  }
  .rule { position: absolute; background: var(--grey); }
  .rule--top { left: 38px; top: 36px; width: 9px; height: 182px; }
  .rule--price { left: 872px; top: 932px; width: 17px; height: 185px; }
  .headline {
    position: absolute; left: 74px; top: 30px; margin: 0;
    font-family: "Josefin Sans", "Century Gothic", sans-serif; font-weight: 700;
    font-size: 54px; line-height: 67px; letter-spacing: 1px; text-transform: uppercase;
    white-space: nowrap;
  }
  .headline span { display: block; }
  .headline .accent { color: var(--green); }
  .tagline {
    position: absolute; left: 34px; top: 248px; margin: 0;
    font-family: "Homemade Apple", cursive; font-weight: 400;
    font-size: 54px; line-height: 90px; color: var(--gold); white-space: nowrap;
  }
  .intro {
    position: absolute; left: 37px; top: 383px; margin: 0;
    font-weight: 400; font-size: 21px; color: var(--green); text-transform: uppercase; letter-spacing: .3px;
    white-space: nowrap;
  }
  .feature { position: absolute; left: 34px; width: 740px; display: flex; }
  .feature__num {
    flex: 0 0 86px; text-align: center; font-weight: 400; font-size: 60px; line-height: 72px;
  }
  .feature__text {
    font-weight: 300; font-size: 23px; line-height: 36px; color: var(--body);
    margin: 0; padding-top: 1px; white-space: nowrap;
  }
  .num-grey { color: #b3b3b3; }
  .num-gold { color: var(--gold); font-weight: 700; }
  .num-green { color: var(--green); }
  .perks {
    position: absolute; left: 120px; top: 732px; margin: 0; padding: 0; list-style: none;
    font-weight: 300; font-size: 17px; line-height: 24.5px; color: var(--gold); white-space: nowrap;
  }
  .perks li::before { content: "- "; }
  .perks .cont { padding-left: 8px; }
  .perks .cont::before { content: ""; }
  .runner {
    position: absolute; left: 590px; top: 494px; width: 300px; height: 398px;
    background: linear-gradient(160deg, #555 0%, var(--silhouette) 100%);
    border-radius: 40% 40% 30% 30%;
  }
  .brand {
    position: absolute; left: 36px; top: 934px; width: 214px; height: 177px;
    background: #0b0b0b; display: flex; align-items: center; justify-content: center; gap: 8px;
  }
  .brand__dot { width: 12px; height: 12px; border-radius: 50%; background: var(--gold); }
  .brand__name { font-weight: 400; font-size: 30px; color: var(--green); white-space: nowrap; }
  .offer {
    position: absolute; right: 80px; top: 934px; margin: 0; text-align: right;
    font-family: "Josefin Sans", "Century Gothic", sans-serif; font-weight: 700;
    font-size: 52px; line-height: 67px; letter-spacing: 1px; text-transform: uppercase;
    white-space: nowrap;
  }
  .offer span { display: block; }
  .offer .accent { color: var(--green); }
  .contact {
    position: absolute; left: 0; right: 0; top: 1164px; margin: 0; text-align: center;
    font-weight: 400; font-size: 22px; color: var(--gold);
  }
</style>
</head>
<body>
<main class="flyer">
  <div class="rule rule--top"></div>
  <h1 class="headline">
    <span>Get a Brisk Peak Form.</span>
    <span>Live a Brisk Peak Life.</span>
    <span class="accent">In Just 12 Weeks.</span>
  </h1>
  <p class="tagline">take the challenge today!</p>

  <p class="intro">Your challenge, should you choose to accept it, will include:</p>

  <div class="feature" style="top:420px">
    <div class="feature__num num-grey">3</div>
    <p class="feature__text">weekly one-hour group training sessions using fast, high intensity<br>&amp; seriously fun cardio workouts with music to pump you up</p>
  </div>
  <div class="feature" style="top:498px">
    <div class="feature__num num-gold">90</div>
    <p class="feature__text">day weight management &amp; nutrition plan using revolutionary<br>nutritional, all natural products (all products included)</p>
  </div>
  <div class="feature" style="top:576px">
    <div class="feature__num num-grey">12</div>
    <p class="feature__text">week E-Course covering the dieting dilemma,<br>exercise, stress management and sleep</p>
  </div>
  <div class="feature" style="top:655px">
    <div class="feature__num num-green">1</div>
    <p class="feature__text">Personalised &amp; interactive online<br>membership program which includes:</p>
  </div>

  <ul class="perks">
    <li>Customised meal plans based on your personal</li>
    <li class="cont">nutrition parameters &amp; food preferences</li>
    <li>Step by Step guide to achieving your health goals</li>
    <li>Interactive goal setting charts to track your progress</li>
    <li>Delicious recipe database &amp; thousands of meal options</li>
    <li>Easy interactive nutrition and exercise journal</li>
    <li>Full nutrition support from our team of experts</li>
  </ul>

  <div class="runner" role="img" aria-label="Grey silhouette of a woman running"></div>

  <div class="brand">
    <span class="brand__dot"></span>
    <span class="brand__name">Vantle Racquet</span>
  </div>

  <p class="offer">
    <span>Only $99 per week.</span>
    <span>Starts Sept 17.</span>
    <span class="accent">Join Today!</span>
  </p>
  <div class="rule rule--price"></div>

  <p class="contact">Call 02 7381 2459 or email us at info@vantleracquet.example</p>
</main>
</body>
</html>
```